New School header and footer

Our school needs a modern new header and a matching footer. Currently we have the school logo, name and contact with no graphics at all (attached).
I have also attached another version of the school logo which is on our school sign.
The school's logo is a Swift (Apus pacificus) (bird) see http://www.findora-web.com.au/search?q=Apus+pacificus&safe=active&hl=en-AU&gbv=2&prmd=ivns&source=lnms&tbm=isch&sa=X&ei=Xg0-U4v4JYmulQWq1YCADw&ved=0CAUQ_AU

The school is located in North Queensland Australia near the town of Ingham it was established in 1922

I would like the header/footer to have:
The school name- Merivale State School
School moto - Opportunity through endeavour
contact details: Address Phone Fax website and principal email (some of these things could be in the footer) these details are in the uploaded files
The logo or elements of the logo (as is or modified to modernise)

School website is https://merivaless.qx.edu.au

The header and footer would be used on A4 paper with microsoft word it will be used for the school newsletter and in all official school documents.

It can be colour or black and white. School uniforms are have light blue some dark blue and white the colours in the design are not limited to these colours.
Updates

Thanks to those people who have already submitted designs. I have made some additions to the brief in the should have and should not have sections and also the sliding scale thing. I hope that helps.

There are a lot of designs thankyou all so much. Some feedback from my staff is that we really need to keep the traditional logo of the bird from the website. It doesn't have to have the words around it but the shape and position needs to stay the same. I thought we were ready to change modernise the logo but unfortunately they aren't ready. However the rest of the design needs to be modern, less rigid and square. There is one square design that I did like and they have made the changes required. I will choose the designs I like and should be putting them up for online voting next week.
Just a side note a large tropical cyclone is moving close to our community. We are not at risk right now but it is possible that we will experience flooding and maybe loss of power so if there is a delay in posting the results this will probably be the reason.  I will try to respond to last minute questions or design submissions but I'll be pretty busy preparing my home and the school for the possibility of this weather event. Once again thankyou for your submissions I have been impressed by the quailty of the submissions from this particular design crowd.

Target Market(s)

For a school used in official documents, letters, and newsletters.

My staff will be choosing the winner.

Industry/Entity Type

School

Requirements
Must have
• School name
School motto
Address
Phone
Fax
Website URL
Header and footer
Should not have
• Avoid large amounts of block colours this letter head will be used in colour format most of the time but will be photo copied and faxed from time to time.

```html
<!DOCTYPE html>
<html lang="en">
<head>
<meta charset="utf-8">
<title>Merivale State School Letterhead</title>
<link rel="stylesheet" href="https://fonts.googleapis.com/css2?family=Marcellus&family=Crimson+Text:wght@600&display=swap">
<style>
  :root {
    --backdrop: #262262;
    --paper: #ffffff;
    --ink: #111111;
    --rule: #333333;
    --faint: #d6d6d8;
  }
  html, body {
    margin: 0;
    padding: 0;
    width: 1200px;
    height: 900px;
    overflow: hidden;
    background: var(--backdrop);
  }
  .letterhead {
    position: absolute;
    left: 390px;
    top: 152px;
    width: 421px;
    height: 596px;
    background: var(--paper);
  }
  .school-mark {
    position: absolute;
    left: 22px;
    top: 20px;
    width: 74px;
    height: 74px;
    border-radius: 50%;
    border: 1.5px solid var(--ink);
    box-sizing: border-box;
    display: flex;
    align-items: center;
    justify-content: center;
    text-align: center;
    font-family: "Marcellus", serif;
    font-size: 10px;
    line-height: 1.15;
    color: var(--ink);
  }
  .masthead {
    position: absolute;
    left: 108px;
    top: 31px;
    width: 280px;
    text-align: center;
  }
  .school-name {
    margin: 0;
    padding: 3px 0 2px;
    border-top: 1px solid var(--rule);
    border-bottom: 1px solid var(--rule);
    font-family: "Marcellus", serif;
    font-weight: 400;
    font-size: 22.5px;
    letter-spacing: 0.2px;
    line-height: 1.1;
    color: var(--ink);
    white-space: nowrap;
  }
  .postal-address,
  .school-motto {
    margin: 4px 0 0;
    font-family: "Crimson Text", serif;
    font-weight: 600;
    font-size: 7.4px;
    line-height: 1.2;
    color: var(--ink);
    white-space: nowrap;
  }
  .school-motto {
    margin-top: 2px;
    letter-spacing: 0.4px;
  }
  .watermark {
    position: absolute;
    left: 118px;
    top: 232px;
    width: 176px;
    height: 176px;
    border-radius: 50%;
    border: 2px solid var(--faint);
    box-sizing: border-box;
    display: flex;
    align-items: center;
    justify-content: center;
    text-align: center;
    font-family: "Marcellus", serif;
    font-size: 22px;
    line-height: 1.15;
    color: var(--faint);
  }
  .contact-footer {
    position: absolute;
    left: 0;
    right: 0;
    top: 571px;
    border-top: 1px solid var(--rule);
    padding-top: 3px;
    text-align: center;
    font-family: "Crimson Text", serif;
    font-weight: 600;
    font-size: 6.8px;
    line-height: 1.2;
    color: var(--ink);
    white-space: nowrap;
  }
  .contact-footer span + span { margin-left: 5px; }
</style>
</head>
<body>
  <main class="letterhead">
    <div class="school-mark">Merivale<br>State<br>School</div>
    <header class="masthead">
      <h1 class="school-name">MERIVALE STATE SCHOOL</h1>
      <p class="postal-address">Canefield Road Merivale 4861 PO Box 512 Kelsey 4861</p>
      <p class="school-motto">Opportunity through endeavour</p>
    </header>
    <div class="watermark" aria-hidden="true">Merivale<br>State<br>School</div>
    <footer class="contact-footer">
      <span>Phone: 4700 5512</span><span>Fax: 4700 5519</span><span>Email: theprincipal@merivaless.qx.edu.au</span><span>Web: https://merivaless.qx.edu.au</span>
    </footer>
  </main>
</body>
</html>
```